PHD-project

i need the figures to be in the same stile. info is inside the file. There are 5 figures that need redesign. this is for PhD.

Target Market(s)

it will be used in my phd

Colors

Designer to choose colors to be used in the design.

```html
<!DOCTYPE html>
<html lang="en">
<head>
<meta charset="UTF-8">
<title>Research Timeline 2012–2017</title>
<link href="https://fonts.googleapis.com/css2?family=Quicksand:wght@500;600;700&display=swap" rel="stylesheet">
<style>
  :root {
    --bg: #ffffff;
    --ink: #1f1f1f;
    --stem: #bdbdbd;
    --node-ring: #c9c9c9;
    --band-light: #5b97b5;
    --band-mid: #2a77a3;
    --band-deep: #1b5b89;
    --line-start: #8fc1de;
    --line-end: #0c3c69;
    --photo-a: #d9dde2;
    --photo-b: #b7bec8;
  }
  * { margin: 0; padding: 0; box-sizing: border-box; }
  html, body {
    width: 1200px; height: 678px; overflow: hidden;
    background: var(--bg);
    font-family: "Quicksand", sans-serif;
    color: var(--ink);
  }
  .timeline { position: relative; width: 1200px; height: 678px; }
  .axis { position: absolute; left: 0; top: 0; }

  .milestone-card {
    position: absolute; width: 116px;
  }
  .milestone-card .year {
    height: 35px; display: flex; align-items: center; justify-content: center;
    color: #fff; font-weight: 600; font-size: 21px; letter-spacing: 0.2px;
    position: relative;
  }
  .milestone-card .photo { height: 115px; }
  .card-top .year { border-radius: 0 0 9px 9px; }
  .card-top .year::after {
    content: ""; position: absolute; left: 50%; bottom: -14px; transform: translateX(-50%);
    border-left: 15px solid transparent; border-right: 15px solid transparent;
    border-top: 15px solid var(--band-color);
  }
  .card-bottom .year { border-radius: 9px 9px 0 0; }
  .card-bottom .year::before {
    content: ""; position: absolute; left: 50%; top: -14px; transform: translateX(-50%);
    border-left: 15px solid transparent; border-right: 15px solid transparent;
    border-bottom: 15px solid var(--band-color);
  }
  .year { background: var(--band-color); }

  .band-light { --band-color: var(--band-light); }
  .band-mid { --band-color: var(--band-mid); }
  .band-deep { --band-color: var(--band-deep); }

  .photo-meeting { background: linear-gradient(160deg, #e9edf0, #c9cfd6 55%, #e79a3f 100%); }
  .photo-portrait { background: linear-gradient(180deg, #e6e8ea, #a7adb4 70%, #c8b295); }
  .photo-laptop { background: linear-gradient(150deg, #8b7766, #d8c2ae 50%, #8a8d92); }
  .photo-interview { background: linear-gradient(160deg, #d8cfc8, #b99a8c 50%, #50505a); }
  .photo-document { background: linear-gradient(160deg, #efe6e2, #d3cbc5 55%, #8c8f96); }

  .label {
    position: absolute; width: 180px; text-align: center;
    font-size: 16.5px; font-weight: 500; line-height: 22px;
  }
  .label sup { font-size: 9px; vertical-align: 7px; line-height: 0; }
</style>
</head>
<body>
<div class="timeline">
  <svg class="axis" width="1200" height="678" viewBox="0 0 1200 678" aria-hidden="true">
    <defs>
      <linearGradient id="axisGradient" x1="100" y1="0" x2="1108" y2="0" gradientUnits="userSpaceOnUse">
        <stop offset="0" stop-color="var(--line-start)"/>
        <stop offset="0.45" stop-color="#2c78a5"/>
        <stop offset="1" stop-color="var(--line-end)"/>
      </linearGradient>
    </defs>
    <rect x="100" y="337" width="1008" height="8" fill="url(#axisGradient)"/>
    <line x1="100" y1="341" x2="1108" y2="341" stroke="#ffffff" stroke-width="1" stroke-dasharray="9 5" opacity="0.85"/>

    <g stroke="var(--stem)" stroke-width="1.6" fill="var(--stem)">
      <line x1="184" y1="305" x2="184" y2="333"/><circle cx="184" cy="305" r="2.6" stroke="none"/>
      <line x1="520" y1="305" x2="520" y2="333"/><circle cx="520" cy="305" r="2.6" stroke="none"/>
      <line x1="352" y1="349" x2="352" y2="376"/><circle cx="352" cy="376" r="2.6" stroke="none"/>
      <line x1="688" y1="349" x2="688" y2="376"/><circle cx="688" cy="376" r="2.6" stroke="none"/>
      <line x1="1024" y1="349" x2="1024" y2="376"/><circle cx="1024" cy="376" r="2.6" stroke="none"/>
    </g>

    <g fill="#ffffff" stroke="var(--node-ring)" stroke-width="3">
      <circle cx="184" cy="341" r="7.5"/>
      <circle cx="352" cy="341" r="7.5"/>
      <circle cx="520" cy="341" r="7.5"/>
      <circle cx="688" cy="341" r="7.5"/>
      <circle cx="1024" cy="341" r="7.5"/>
    </g>
  </svg>

  <!-- upper labels -->
  <div class="label" style="left:94px; top:226px;">Prequel with<br>Student-led<br>Innovation</div>
  <div class="label" style="left:430px; top:270px;">Interventions</div>

  <!-- lower labels -->
  <div class="label" style="left:262px; top:387px;">1<sup>st</sup> Round of<br>Interviews</div>
  <div class="label" style="left:598px; top:387px;">2<sup>nd</sup> Round of<br>Interviews</div>
  <div class="label" style="left:934px; top:387px;">Additional<br>Interviews &amp;<br>Comments</div>

  <!-- cards above axis -->
  <div class="milestone-card card-top band-mid" style="left:294px; top:162px;">
    <div class="photo photo-portrait" role="img" aria-label="Photo of a candidate in a blazer seated at a desk for an interview"></div>
    <div class="year">2013</div>
  </div>
  <div class="milestone-card card-top band-mid" style="left:630px; top:162px;">
    <div class="photo photo-interview" role="img" aria-label="Photo of an interview across a table with a clipboard"></div>
    <div class="year">2015</div>
  </div>
  <div class="milestone-card card-top band-deep" style="left:966px; top:162px;">
    <div class="photo photo-document" role="img" aria-label="Photo of hands reviewing and commenting on a printed document"></div>
    <div class="year">2017</div>
  </div>

  <!-- cards below axis -->
  <div class="milestone-card card-bottom band-light" style="left:126px; top:370px;">
    <div class="year">2012</div>
    <div class="photo photo-meeting" role="img" aria-label="Photo of students working together with laptops around a table"></div>
  </div>
  <div class="milestone-card card-bottom band-mid" style="left:462px; top:370px;">
    <div class="year">2013-2015</div>
    <div class="photo photo-laptop" role="img" aria-label="Photo of hands typing on a laptop beside a notebook"></div>
  </div>
</div>
</body>
</html>
```